PIPEWELLS HOT WATER CYLINDER STICKER – PRINT LAYOUT

SECTION 1 – HOMEOWNER MAINTENANCE GUIDE (Boxed Section):
πŸ“– Hot Water Cylinder Maintenance
βœ… Monthly: Quick visual check for leaks, rust, or pooling water.
βœ… Every 6 Months: Test your TPR (Temperature & Pressure Relief) valve.
β€’ Lift the lever gently until water flows, then release.
β€’ If it’s blocked or constantly dripping – call us immediately.
βœ… Listen: Popping, banging, or rumbling? Could be sediment build-up.
βœ… Annually: Book a professional service to check anode, thermostat & valves.

SECTION 2 – WARNING SIGNS (Highlight Box or Red Accent):
🚨 Call Us Immediately If You Notice:
β€’ No hot water or inconsistent temperature
β€’ Water leaking from tank or pipes
β€’ Rust-coloured water
β€’ Sudden drop in water pressure

SECTION 3 – CALL TO ACTION (Large & Bold):
πŸ“ž NEED HELP FAST? CALL PIPEWELLS FIRST!
πŸ“² PHONE: [0437 218 965] (largest text on sticker)
🌐 [www.pipewells.com.au]

FOOTER (Small Print):
Fully Licensed & Insured | QBCC 26481039 | 24/7 Emergency Service
This guide is for general maintenance only. For all repairs or safety concerns, contact a licensed plumber.

βœ… DESIGN RECOMMENDATIONS
β€’ Size: 27cm long x 10cm wide works well (large enough to read easily when standing).
β€’ Material: Waterproof vinyl with strong adhesive.
β€’ Colors:
o Header & Call-to-Action in your brand colors
o Maintenance guide in a light-shaded box for contrast
o Warning signs section with red accent or icon to grab attention
β€’ Icons: Use βœ… πŸ“– 🚨 πŸ“ž for quick scanning.

```html
<!DOCTYPE html>
<html lang="en">
<head>
<meta charset="utf-8">
<title>Pipewells Hot Water Cylinder Sticker – Print Layout</title>
<link rel="stylesheet" href="https://fonts.googleapis.com/css2?family=Barlow+Semi+Condensed:wght@500;600;700&family=Roboto+Condensed:wght@400;500;700&display=swap">
<style>
:root{
  --navy:#0c4d8a;
  --sky:#1cb0e2;
  --frame-blue:#29a9df;
  --brown-dark:#6a4320;
  --brown-light:#c2a77f;
  --orange:#f05a22;
  --orange-deep:#d94a1c;
  --orange-text:#f26522;
  --grey:#5b5b5b;
  --grey-dark:#4d4d4d;
  --ink:#1e1e1e;
  --paper:#ffffff;
}
*{box-sizing:border-box;margin:0;padding:0}
html,body{width:1200px;height:1200px;overflow:hidden;background:var(--paper)}
body{font-family:"Roboto Condensed",Arial,sans-serif;color:var(--ink)}
.stage{position:relative;width:1050px;height:1050px;transform:scale(1.142857);transform-origin:0 0}

.dimensions{position:absolute;left:0;top:0}
.dim-label{position:absolute;font-family:"Roboto Condensed",Arial,sans-serif;font-size:22px;color:#222;background:var(--paper);padding:0 8px}

.sticker{position:absolute;width:926px;height:344px;background:var(--paper)}
.sticker--proof{left:32px;top:133px;border:2px solid #111}
.sticker--print{left:62px;top:591px}
.sticker--proof > *{margin:-2px 0 0 -2px}

.heading{font-family:"Barlow Semi Condensed",Arial,sans-serif;font-weight:600;color:#fff;letter-spacing:1.2px;font-size:21px;line-height:30px;padding-left:40px;height:30px}

/* maintenance guide */
.guide{position:absolute;left:15px;top:14px;width:538px;height:223px;border:2px solid var(--frame-blue);border-top:0}
.guide .heading{margin:0 -2px;background:linear-gradient(90deg,var(--navy),var(--sky))}
.guide-sub{position:absolute;left:9px;top:39px;width:398px;height:21px;background:linear-gradient(90deg,var(--brown-dark),var(--brown-light));clip-path:polygon(0 0,94% 0,100% 100%,0 100%);color:#fff;font-family:"Barlow Semi Condensed",Arial,sans-serif;font-weight:500;font-size:15px;letter-spacing:1.4px;line-height:21px;padding-left:28px}
.task{position:absolute;left:12px;display:flex;align-items:center;font-size:15.5px;white-space:nowrap}
.tick{width:17px;height:17px;margin-right:6px;flex:none}
.tag{background:linear-gradient(90deg,var(--navy),var(--sky));color:#fff;font-size:13.5px;line-height:18px;height:18px;padding:0 14px 0 6px;clip-path:polygon(0 0,100% 0,88% 100%,0 100%);margin-right:4px}
.step{position:absolute;left:38px;font-size:15.5px;display:flex;align-items:center;white-space:nowrap}
.step::before{content:"";width:0;height:0;border-left:8px solid var(--frame-blue);border-top:5px solid transparent;border-bottom:5px solid transparent;margin-right:14px}

/* brand + footer */
.brand{position:absolute;left:23px;top:250px;display:flex;align-items:center;gap:12px}
.brand-mark{width:34px;height:34px;border-radius:50%;background:var(--frame-blue)}
.brand-name{font-family:"Barlow Semi Condensed",Arial,sans-serif;font-weight:700;font-size:31px;color:var(--grey);line-height:30px;letter-spacing:.5px}
.brand-trades{font-family:"Barlow Semi Condensed",Arial,sans-serif;font-weight:500;font-size:13.5px;color:var(--grey);letter-spacing:.5px}
.licence{position:absolute;left:283px;top:244px;width:270px;height:40px;background:var(--grey);clip-path:polygon(9% 0,100% 0,100% 100%,0 100%);color:#fff;font-size:13px;line-height:15px;text-align:center;padding:5px 2px 0 24px}
.disclaimer{position:absolute;left:283px;top:290px;width:270px;height:47px;background:var(--grey-dark);clip-path:polygon(0 0,100% 0,100% 100%,0 100%);color:#fff;font-size:13px;line-height:14.5px;padding:3px 8px 0 5px;text-align:justify;letter-spacing:.2px}
.bleed-band{position:absolute;left:-10px;top:334px;width:562px;height:25px;background:var(--grey)}

/* warning */
.warning{position:absolute;left:565px;top:14px;width:345px;height:158px;border:2px solid var(--orange);border-top:0}
.warning .heading{margin:0 -2px;padding-left:12px;background:linear-gradient(90deg,var(--orange-deep),var(--orange))}
.warning-badge{position:absolute;right:-2px;top:0;width:58px;height:48px;background:var(--orange);clip-path:polygon(30% 0,100% 0,100% 100%,0 100%,0 64%)}
.warning-badge svg{position:absolute;right:6px;top:6px}
.warning-sub{position:absolute;left:7px;top:40px;width:276px;height:22px;background:var(--grey);clip-path:polygon(0 0,92% 0,100% 100%,0 100%);color:#fff;font-size:15px;line-height:22px;padding-left:9px}
.signs{position:absolute;left:14px;top:70px;list-style:none}
.signs li{display:flex;align-items:center;font-size:16px;line-height:20px;white-space:nowrap}
.signs svg{margin-right:9px}

/* call to action */
.cta{position:absolute;left:565px;top:186px;width:345px;height:146px;border:2px solid var(--frame-blue);border-top:0}
.cta .heading{margin:0 -2px;padding-left:14px;background:linear-gradient(90deg,var(--sky),var(--navy))}
.cta-mark{position:absolute;left:14px;top:57px;width:34px;height:34px;border-radius:50%;background:var(--frame-blue)}
.cta-rule{position:absolute;left:66px;top:38px;width:1.5px;height:96px;background:var(--brown-light)}
.cta-ask{position:absolute;left:70px;top:37px;width:265px;text-align:center;font-family:"Barlow Semi Condensed",Arial,sans-serif;font-weight:700;letter-spacing:1.5px}
.cta-ask .fast{color:var(--frame-blue);font-size:15.5px;line-height:18px}
.cta-ask .first{color:var(--ink);font-size:15px;line-height:18px;font-weight:600}
.cta-phone{position:absolute;left:80px;top:76px;display:flex;align-items:center}
.phone-icon{display:flex;flex-direction:column;align-items:center;font-size:7.5px;color:var(--ink);margin-right:8px}
.phone-number{font-family:"Roboto Condensed",Arial,sans-serif;font-weight:700;font-size:39px;color:var(--orange-text);letter-spacing:.5px;line-height:40px}
.cta-web{position:absolute;left:92px;top:117px;display:flex;align-items:center;font-size:16px;gap:6px}
</style>
</head>
<body>
<main class="stage">

  <svg class="dimensions" width="1050" height="1050" viewBox="0 0 1050 1050" aria-hidden="true">
    <g stroke="#333" stroke-width="1.5" fill="#333">
      <line x1="34" y1="75" x2="946" y2="75"/>
      <polygon points="28,75 40,70 40,80"/>
      <polygon points="952,75 940,70 940,80"/>
      <line x1="1000" y1="138" x2="1000" y2="472"/>
      <polygon points="1000,132 995,144 1005,144"/>
      <polygon points="1000,478 995,466 1005,466"/>
      <!-- crop marks -->
      <line x1="61" y1="553" x2="61" y2="583"/>
      <line x1="988" y1="553" x2="988" y2="583"/>
      <line x1="61" y1="950" x2="61" y2="974"/>
      <line x1="988" y1="950" x2="988" y2="974"/>
      <line x1="22" y1="590" x2="52" y2="590"/>
      <line x1="996" y1="590" x2="1026" y2="590"/>
      <line x1="22" y1="936" x2="52" y2="936"/>
      <line x1="996" y1="936" x2="1026" y2="936"/>
    </g>
  </svg>
  <span class="dim-label" style="left:450px;top:60px">27cm</span>
  <span class="dim-label" style="left:960px;top:289px">10 cm</span>

  <!-- ===== Sticker: proof with trim line ===== -->
  <section class="sticker sticker--proof">
    <div class="guide">
      <h2 class="heading">HOMEOWNER MAINTENANCE GUIDE</h2>
      <div class="guide-sub">Hot Water Cylinder Maintenance</div>
      <div class="task" style="top:70px"><svg class="tick" viewBox="0 0 17 17"><rect x="1" y="3" width="13" height="13" fill="none" stroke="#1e8fd0" stroke-width="1.8"/><path d="M4 9l3.5 3.5L16 2" fill="none" stroke="#1e8fd0" stroke-width="2.4"/></svg><span class="tag">Monthly:</span>Quick visual check for leaks, rust, or pooling water.</div>
      <div class="task" style="top:100px"><svg class="tick" viewBox="0 0 17 17"><rect x="1" y="3" width="13" height="13" fill="none" stroke="#1e8fd0" stroke-width="1.8"/><path d="M4 9l3.5 3.5L16 2" fill="none" stroke="#1e8fd0" stroke-width="2.4"/></svg><span class="tag">Every 6 Months:</span>Test your TPR (Temperature &amp; Pressure Relief) valve.</div>
      <div class="step" style="top:125px">Lift the lever gently until water flows, then release.</div>
      <div class="step" style="top:146px">If it’s blocked or constantly dripping – call us immediately.</div>
      <div class="task" style="top:167px"><svg class="tick" viewBox="0 0 17 17"><rect x="1" y="3" width="13" height="13" fill="none" stroke="#1e8fd0" stroke-width="1.8"/><path d="M4 9l3.5 3.5L16 2" fill="none" stroke="#1e8fd0" stroke-width="2.4"/></svg><span class="tag">Listen:</span>Popping, banging, or rumbling? Could be sediment build-up.</div>
      <div class="task" style="top:195px"><svg class="tick" viewBox="0 0 17 17"><rect x="1" y="3" width="13" height="13" fill="none" stroke="#1e8fd0" stroke-width="1.8"/><path d="M4 9l3.5 3.5L16 2" fill="none" stroke="#1e8fd0" stroke-width="2.4"/></svg><span class="tag">Annually:</span>Book a professional service to check anode, thermostat &amp; valves.</div>
    </div>

    <div class="brand">
      <span class="brand-mark"></span>
      <div><div class="brand-name">PIPEWELLS</div><div class="brand-trades">PLUMBING | DRAINAGE | GAS</div></div>
    </div>
    <div class="licence">Fully Licensed &amp; Insured | QBCC 26481039 | 24/7 Emergency Service</div>
    <div class="disclaimer">This guide is for general maintenance only. For all repairs or safety concerns, contact a licensed plumber.</div>

    <div class="warning">
      <h2 class="heading">WARNING SIGNS</h2>
      <div class="warning-badge"><svg width="40" height="36" viewBox="0 0 40 36"><path d="M20 3L37 33H3Z" fill="none" stroke="#fff" stroke-width="3" stroke-linejoin="round"/><rect x="18.3" y="13" width="3.4" height="11" fill="#fff"/><rect x="18.3" y="26.5" width="3.4" height="3.4" fill="#fff"/></svg></div>
      <div class="warning-sub">Call Us Immediately If You Notice:</div>
      <ul class="signs">
        <li><svg width="18" height="10" viewBox="0 0 18 10"><path d="M0 0l7 5-7 5zM8 0l7 5-7 5z" fill="#f05a22"/></svg>No hot water or inconsistent temperature</li>
        <li><svg width="18" height="10" viewBox="0 0 18 10"><path d="M0 0l7 5-7 5zM8 0l7 5-7 5z" fill="#f05a22"/></svg>Water leaking from tank or pipes</li>
        <li><svg width="18" height="10" viewBox="0 0 18 10"><path d="M0 0l7 5-7 5zM8 0l7 5-7 5z" fill="#f05a22"/></svg>Rust-coloured water</li>
        <li><svg width="18" height="10" viewBox="0 0 18 10"><path d="M0 0l7 5-7 5zM8 0l7 5-7 5z" fill="#f05a22"/></svg>Sudden drop in water pressure</li>
      </ul>
    </div>

    <div class="cta">
      <h2 class="heading">CALL TO ACTION</h2>
      <span class="cta-mark"></span>
      <span class="cta-rule"></span>
      <div class="cta-ask"><div class="fast">NEED HELP FAST?</div><div class="first">CALL PIPEWELLS FIRST!</div></div>
      <div class="cta-phone">
        <span class="phone-icon"><svg width="18" height="16" viewBox="0 0 18 16"><path d="M1 5c0-3 16-3 16 0v2h-4V5H5v2H1z" fill="#f05a22"/><rect x="3" y="8" width="12" height="7" rx="1.5" fill="#f05a22"/><circle cx="9" cy="11.5" r="2" fill="#fff"/></svg>PHONE</span>
        <span class="phone-number">0437 218 965</span>
      </div>
      <div class="cta-web"><svg width="20" height="20" viewBox="0 0 20 20" fill="none" stroke="#1e8fd0" stroke-width="1.6"><circle cx="10" cy="10" r="8.5"/><ellipse cx="10" cy="10" rx="3.8" ry="8.5"/><path d="M1.5 10h17M3 5.5h14M3 14.5h14"/></svg>www.pipewells.com.au</div>
    </div>
  </section>

  <!-- ===== Sticker: print file with bleed ===== -->
  <section class="sticker sticker--print">
    <div class="bleed-band"></div>
    <div class="guide">
      <h2 class="heading">HOMEOWNER MAINTENANCE GUIDE</h2>
      <div class="guide-sub">Hot Water Cylinder Maintenance</div>
      <div class="task" style="top:70px"><svg class="tick" viewBox="0 0 17 17"><rect x="1" y="3" width="13" height="13" fill="none" stroke="#1e8fd0" stroke-width="1.8"/><path d="M4 9l3.5 3.5L16 2" fill="none" stroke="#1e8fd0" stroke-width="2.4"/></svg><span class="tag">Monthly:</span>Quick visual check for leaks, rust, or pooling water.</div>
      <div class="task" style="top:100px"><svg class="tick" viewBox="0 0 17 17"><rect x="1" y="3" width="13" height="13" fill="none" stroke="#1e8fd0" stroke-width="1.8"/><path d="M4 9l3.5 3.5L16 2" fill="none" stroke="#1e8fd0" stroke-width="2.4"/></svg><span class="tag">Every 6 Months:</span>Test your TPR (Temperature &amp; Pressure Relief) valve.</div>
      <div class="step" style="top:125px">Lift the lever gently until water flows, then release.</div>
      <div class="step" style="top:146px">If it’s blocked or constantly dripping – call us immediately.</div>
      <div class="task" style="top:167px"><svg class="tick" viewBox="0 0 17 17"><rect x="1" y="3" width="13" height="13" fill="none" stroke="#1e8fd0" stroke-width="1.8"/><path d="M4 9l3.5 3.5L16 2" fill="none" stroke="#1e8fd0" stroke-width="2.4"/></svg><span class="tag">Listen:</span>Popping, banging, or rumbling? Could be sediment build-up.</div>
      <div class="task" style="top:195px"><svg class="tick" viewBox="0 0 17 17"><rect x="1" y="3" width="13" height="13" fill="none" stroke="#1e8fd0" stroke-width="1.8"/><path d="M4 9l3.5 3.5L16 2" fill="none" stroke="#1e8fd0" stroke-width="2.4"/></svg><span class="tag">Annually:</span>Book a professional service to check anode, thermostat &amp; valves.</div>
    </div>

    <div class="brand">
      <span class="brand-mark"></span>
      <div><div class="brand-name">PIPEWELLS</div><div class="brand-trades">PLUMBING | DRAINAGE | GAS</div></div>
    </div>
    <div class="licence">Fully Licensed &amp; Insured | QBCC 26481039 | 24/7 Emergency Service</div>
    <div class="disclaimer">This guide is for general maintenance only. For all repairs or safety concerns, contact a licensed plumber.</div>

    <div class="warning">
      <h2 class="heading">WARNING SIGNS</h2>
      <div class="warning-badge"><svg width="40" height="36" viewBox="0 0 40 36"><path d="M20 3L37 33H3Z" fill="none" stroke="#fff" stroke-width="3" stroke-linejoin="round"/><rect x="18.3" y="13" width="3.4" height="11" fill="#fff"/><rect x="18.3" y="26.5" width="3.4" height="3.4" fill="#fff"/></svg></div>
      <div class="warning-sub">Call Us Immediately If You Notice:</div>
      <ul class="signs">
        <li><svg width="18" height="10" viewBox="0 0 18 10"><path d="M0 0l7 5-7 5zM8 0l7 5-7 5z" fill="#f05a22"/></svg>No hot water or inconsistent temperature</li>
        <li><svg width="18" height="10" viewBox="0 0 18 10"><path d="M0 0l7 5-7 5zM8 0l7 5-7 5z" fill="#f05a22"/></svg>Water leaking from tank or pipes</li>
        <li><svg width="18" height="10" viewBox="0 0 18 10"><path d="M0 0l7 5-7 5zM8 0l7 5-7 5z" fill="#f05a22"/></svg>Rust-coloured water</li>
        <li><svg width="18" height="10" viewBox="0 0 18 10"><path d="M0 0l7 5-7 5zM8 0l7 5-7 5z" fill="#f05a22"/></svg>Sudden drop in water pressure</li>
      </ul>
    </div>

    <div class="cta">
      <h2 class="heading">CALL TO ACTION</h2>
      <span class="cta-mark"></span>
      <span class="cta-rule"></span>
      <div class="cta-ask"><div class="fast">NEED HELP FAST?</div><div class="first">CALL PIPEWELLS FIRST!</div></div>
      <div class="cta-phone">
        <span class="phone-icon"><svg width="18" height="16" viewBox="0 0 18 16"><path d="M1 5c0-3 16-3 16 0v2h-4V5H5v2H1z" fill="#f05a22"/><rect x="3" y="8" width="12" height="7" rx="1.5" fill="#f05a22"/><circle cx="9" cy="11.5" r="2" fill="#fff"/></svg>PHONE</span>
        <span class="phone-number">0437 218 965</span>
      </div>
      <div class="cta-web"><svg width="20" height="20" viewBox="0 0 20 20" fill="none" stroke="#1e8fd0" stroke-width="1.6"><circle cx="10" cy="10" r="8.5"/><ellipse cx="10" cy="10" rx="3.8" ry="8.5"/><path d="M1.5 10h17M3 5.5h14M3 14.5h14"/></svg>www.pipewells.com.au</div>
    </div>
  </section>

</main>
</body>
</html>
```